3 Sympathy Cards for Veterinary Hospital

Hi. Meadowbrook Pet Hospital is a Veterinary Hospital in Australia. We need sympathy cards to send to grieving clients after the loss of their beloved pets.
I have attached the old designs, but we have rebranded and need something to suit our new image.

The cards should have a nice message and appeal to every owner.
They need to match our current branding, but the cards are for the clients, not to advertise us, so not too much branding.
The current cards are attached and they are good because they show a variety of animals so clients might identify with one of them.
I have attached a brown to green gradient that we use on some designs, you don't have to use it, but consider it.
I have attached a logo on background used in some of our new designs, consider using it.
I have attached a font that we use for most new branding.

Target Market(s)

Women 25 to 44

Industry/Entity Type

Veterinary

Font styles to use
Sans Serif
Script

Colors
fac994
cadf82

Requirements
Must have
• IMPORTANT - 3 different designs for the different types of pets.
• 1. Dog.
• 2. Cat.
• 3. Everything else (Rabbits, lizards, ferrets, chickens, birds, mice, rats, snakes)
Nice to have
• Caring and compassionate message.
Should not have
• Too much branding.

```html
<!DOCTYPE html>
<html lang="en">
<head>
<meta charset="utf-8">
<title>Meadowbrook Pet Hospital – Sympathy Cards</title>
<link href="https://fonts.googleapis.com/css2?family=Roboto:wght@400;500&family=Kaushan+Script&display=swap" rel="stylesheet">
<style>
  :root {
    --peach: #fac994;
    --lime: #cadf82;
    --brown: #4a3422;
    --ink: #111111;
    --paper: #ffffff;
    --backdrop: #f3f3f3;
  }
  * { margin: 0; padding: 0; box-sizing: border-box; }
  html, body { width: 960px; height: 1200px; overflow: hidden; }
  body {
    position: relative;
    background: var(--backdrop);
    font-family: "Roboto", Arial, sans-serif;
    color: var(--brown);
  }
  .card {
    position: absolute;
    width: 359px;
    height: 448px;
    background: var(--paper);
    box-shadow: 0 6px 18px rgba(0,0,0,0.08);
  }
  .card--cat { left: 90px; top: 120px; }
  .card--dog { left: 524px; top: 318px; }
  .card--other { left: 80px; top: 630px; }

  .banner {
    position: absolute;
    left: 17px;
    top: 15px;
    width: 326px;
    height: 194px;
  }
  .card--cat .banner { left: 14px; width: 286px; }

  .photo { position: absolute; inset: 0; }
  .photo--cat {
    background:
      radial-gradient(ellipse 45% 40% at 45% 60%, rgba(236,232,226,0.95) 0%, rgba(214,206,196,0.7) 45%, rgba(214,206,196,0) 100%),
      radial-gradient(ellipse 30% 25% at 25% 45%, rgba(150,112,82,0.7) 0%, rgba(150,112,82,0) 100%),
      linear-gradient(180deg, #5e5953 0%, #b7b0a4 22%, #8a8379 40%, #777069 70%, #4f4a45 100%);
  }
  .photo--dog {
    background:
      radial-gradient(ellipse 40% 55% at 38% 45%, #d8954a 0%, #c27a35 35%, rgba(160,95,45,0.6) 65%, rgba(160,95,45,0) 100%),
      radial-gradient(ellipse 25% 30% at 10% 85%, rgba(40,30,24,0.8) 0%, rgba(40,30,24,0) 100%),
      linear-gradient(160deg, #3f4a2c 0%, #6b4a35 30%, #8a4e35 60%, #5a3a2c 100%);
  }

  .seal {
    position: absolute;
    left: 241px;
    top: 55px;
    width: 88px;
    height: 88px;
    border-radius: 50%;
    background: var(--peach);
    border: 2px solid var(--paper);
    box-shadow: 0 0 0 2px var(--peach);
    display: flex;
    flex-direction: column;
    align-items: center;
    justify-content: center;
    color: var(--ink);
  }
  .seal__small { font-size: 8px; letter-spacing: 0.3px; line-height: 1; margin-left: 6px; }
  .seal__large { font-size: 19px; line-height: 1; }

  .dog-message {
    position: absolute;
    right: 10px;
    bottom: 7px;
    text-align: right;
    color: var(--ink);
  }
  .dog-message__small { font-size: 17px; line-height: 1; }
  .dog-message__large { font-size: 36px; line-height: 1; }

  .script-message {
    position: absolute;
    right: 14px;
    bottom: 12px;
    text-align: right;
    color: var(--ink);
  }
  .script-message__script { font-family: "Kaushan Script", cursive; font-size: 30px; line-height: 1; }
  .script-message__caps { font-size: 13px; letter-spacing: 5px; margin-top: 4px; }

  .brand {
    position: absolute;
    left: 0;
    right: 0;
    top: 318px;
    text-align: center;
    font-weight: 500;
    color: var(--brown);
  }
  .brand__dot {
    display: block;
    width: 12px;
    height: 12px;
    border-radius: 50%;
    background: var(--lime);
    margin: 0 auto 6px;
  }
  .brand__line { display: block; font-size: 12px; letter-spacing: 1.5px; line-height: 14px; }
  .brand__line--large { font-size: 21px; letter-spacing: 0.5px; line-height: 24px; }
  .contact {
    position: absolute;
    left: 0;
    right: 0;
    top: 404px;
    text-align: center;
    font-size: 10px;
    line-height: 13px;
    color: var(--brown);
  }
</style>
</head>
<body>

  <section class="card card--cat">
    <div class="banner">
      <div class="photo photo--cat" role="img" aria-label="Photo of a white and brown cat lying on concrete"></div>
      <div class="seal">
        <span class="seal__small">IN HEARTS</span>
        <span class="seal__large">forever</span>
      </div>
    </div>
    <p class="brand"><span class="brand__dot"></span><span class="brand__line">MEADOWBROOK PET</span><span class="brand__line brand__line--large">HOSPITAL</span></p>
    <p class="contact">1800 555 019<br>P.O BOX 812 Greenvale 4070</p>
  </section>

  <section class="card card--dog">
    <div class="banner">
      <div class="photo photo--dog" role="img" aria-label="Photo of a golden retriever in autumn leaves"></div>
      <svg class="photo" viewBox="0 0 326 194" preserveAspectRatio="none" aria-hidden="true">
        <polygon points="237,0 326,0 326,194 170,194" fill="#fac994"/>
      </svg>
      <div class="dog-message">
        <div class="dog-message__small">In hearts</div>
        <div class="dog-message__large">forever</div>
      </div>
    </div>
    <p class="brand"><span class="brand__dot"></span><span class="brand__line">MEADOWBROOK PET</span><span class="brand__line brand__line--large">HOSPITAL</span></p>
    <p class="contact">1800 555 019<br>P.O BOX 812 Greenvale 4070</p>
  </section>

  <section class="card card--other">
    <div class="banner">
      <svg class="photo" viewBox="0 0 326 194" aria-hidden="true">
        <rect width="326" height="194" fill="#fac994"/>
        <polygon points="0,0 326,0 326,50 0,68" fill="#cadf82"/>
      </svg>
      <svg class="photo" viewBox="0 0 326 194">
        <defs>
          <radialGradient id="bird-tones" cx="50%" cy="55%" r="60%">
            <stop offset="0" stop-color="#b59c83"/>
            <stop offset="0.5" stop-color="#e9e4de"/>
            <stop offset="1" stop-color="#fbfaf8"/>
          </radialGradient>
          <radialGradient id="fish-tones" cx="50%" cy="50%" r="60%">
            <stop offset="0" stop-color="#e2522a"/>
            <stop offset="0.35" stop-color="#2a5f86"/>
            <stop offset="1" stop-color="#0f2a44"/>
          </radialGradient>
          <radialGradient id="hamster-tones" cx="50%" cy="55%" r="60%">
            <stop offset="0" stop-color="#e8c9a0"/>
            <stop offset="0.6" stop-color="#cdb39a"/>
            <stop offset="1" stop-color="#9c9590"/>
          </radialGradient>
          <radialGradient id="rooster-tones" cx="45%" cy="45%" r="60%">
            <stop offset="0" stop-color="#e03a2a"/>
            <stop offset="0.6" stop-color="#9e2a1e"/>
            <stop offset="1" stop-color="#5e3b24"/>
          </radialGradient>
          <radialGradient id="snake-tones" cx="50%" cy="50%" r="60%">
            <stop offset="0" stop-color="#9cc94a"/>
            <stop offset="0.55" stop-color="#4f8a2a"/>
            <stop offset="1" stop-color="#1e3a14"/>
          </radialGradient>
        </defs>
        <circle cx="50" cy="85" r="34" fill="url(#bird-tones)" stroke="#ffffff" stroke-width="2" role="img" aria-label="Photo of a small sparrow"/>
        <circle cx="129" cy="56" r="44" fill="url(#fish-tones)" role="img" aria-label="Photo of a red fish underwater"/>
        <circle cx="214" cy="62" r="34" fill="url(#hamster-tones)" role="img" aria-label="Photo of a hamster"/>
        <circle cx="103" cy="141" r="38" fill="url(#rooster-tones)" role="img" aria-label="Photo of a rooster"/>
        <circle cx="177" cy="122" r="32" fill="url(#snake-tones)" role="img" aria-label="Photo of a green snake"/>
      </svg>
      <div class="script-message">
        <div class="script-message__script">In hearts</div>
        <div class="script-message__caps">FOREVER</div>
      </div>
    </div>
    <p class="brand"><span class="brand__dot"></span><span class="brand__line">MEADOWBROOK PET</span><span class="brand__line brand__line--large">HOSPITAL</span></p>
    <p class="contact">1800 555 019<br>P.O BOX 812 Greenvale 4070</p>
  </section>

</body>
</html>
```